Tallgrove Vale Management

I need a professional website. My current website is tallgrovevalemanagement.com and I hate it. It was created with some AI tool very quickly because I needed a site up and running with no advanced notice. I’m open to all designs .. I trust you, the professionals will deliver the results I’m anxiously awaiting! :)

```html
<!DOCTYPE html>
<html lang="en">
<head>
<meta charset="utf-8">
<title>Tallgrove Vale Management</title>
<link rel="stylesheet" href="https://fonts.googleapis.com/css2?family=Inter:wght@300;400;500;600;700;800&display=swap">
<style>
:root{
  --navy:#0f1d35;
  --navy-2:#15243f;
  --navy-card:#17263f;
  --red:#c8102e;
  --red-soft:#e2233f;
  --white:#ffffff;
  --ink:#0f1d35;
  --muted:#7d8797;
  --line:#e9edf2;
  --mist:#e8ecf1;
  --card-border:rgba(255,255,255,.08);
}
*{box-sizing:border-box;margin:0;padding:0}
html,body{width:1200px;height:2386px;overflow:hidden}
body{font-family:"Inter",sans-serif;color:var(--ink);background:var(--white);position:relative}
.accent{color:var(--red)}
/* header + hero */
.hero{position:relative;height:618px;overflow:hidden;background:var(--navy)}
.hero-photo{position:absolute;inset:0;background:
  radial-gradient(ellipse at 62% 52%,rgba(80,82,88,.55) 0,rgba(40,48,66,.35) 30%,rgba(15,29,53,0) 60%),
  linear-gradient(180deg,#1b2438 0%,#1a2336 55%,#141f35 100%)}
.hero-shade{position:absolute;inset:0;background:linear-gradient(90deg,rgba(15,29,53,.75) 0%,rgba(15,29,53,.35) 60%,rgba(15,29,53,.25) 100%)}
.site-header{position:absolute;top:0;left:223px;width:764px;height:48px;display:flex;align-items:center;justify-content:space-between;z-index:2}
.brand{display:flex;align-items:center;gap:6px;color:var(--white);font-weight:700;font-size:10px;letter-spacing:.04em}
.brand-dot{width:10px;height:10px;border-radius:50%;background:var(--red)}
.nav{display:flex;align-items:center;gap:21px}
.nav a{color:#e6e9ef;font-size:10px;text-decoration:none}
.nav .btn-nav{background:var(--red);color:var(--white);font-weight:600;padding:0 17px;height:23px;line-height:23px;border-radius:12px}
.hero-content{position:absolute;left:223px;top:164px;z-index:2;width:420px}
.badge{display:inline-block;height:19px;line-height:19px;padding:0 14px;border-radius:10px;background:rgba(200,16,46,.18);border:1px solid rgba(200,16,46,.35);color:var(--red);font-size:7.5px;font-weight:700;letter-spacing:.14em}
.hero h1{margin-top:12px;font-weight:400;font-size:48px;line-height:51px;color:var(--white);letter-spacing:-.01em}
.hero h1 .accent{color:var(--red-soft)}
.hero p{margin-top:14px;font-size:13px;line-height:21px;color:#d6dbe4;font-weight:300}
.hero-actions{margin-top:22px;display:flex;gap:10px}
.btn{height:36px;border-radius:18px;font-size:11px;font-weight:600;display:flex;align-items:center;justify-content:center;color:var(--white)}
.btn-primary{width:125px;background:var(--red);box-shadow:0 6px 16px rgba(200,16,46,.4)}
.btn-ghost{width:133px;border:1px solid rgba(255,255,255,.7)}
/* sections */
.section-title{font-size:32px;font-weight:400;text-align:center;letter-spacing:-.01em}
.section-sub{font-size:11px;line-height:17px;text-align:center;color:var(--muted);margin:0 auto}
.services{height:455px;position:relative}
.services .section-title{position:absolute;top:688px;top:70px;left:0;right:0}
.services .section-sub{position:absolute;top:119px;left:0;right:0;width:340px}
.service-grid{position:absolute;left:223px;top:189px;display:flex;gap:20px}
.service-card{width:176px;height:214px;border:1px solid var(--line);border-radius:12px;padding:30px 18px 0;box-shadow:0 4px 14px rgba(15,29,53,.04)}
.service-card svg{width:30px;height:30px;display:block}
.service-card h3{margin-top:18px;font-size:12.5px;font-weight:600}
.service-card p{margin-top:10px;font-size:9.6px;line-height:16.6px;color:var(--muted)}
.service-card .more{margin-top:10px;display:block;font-size:9px;font-weight:600;color:var(--red)}
.dashboard{height:438px;background:linear-gradient(160deg,#0f1d35 0%,#121f3a 60%,#182240 100%);position:relative;color:var(--white)}
.dashboard .section-title{position:absolute;top:71px;left:0;right:0}
.dashboard .section-sub{position:absolute;top:121px;left:0;right:0;color:#b6bfcd}
.stat{position:absolute;width:215px;height:94px;background:var(--navy-card);border:1px solid var(--card-border);border-radius:10px;padding:20px 15px 0}
.stat .value{font-size:21px;font-weight:700}
.stat .label{margin-top:6px;font-size:8.5px;color:#b9c1ce}
.stat .bar{margin-top:11px;height:2px;background:rgba(255,255,255,.08)}
.stat .bar span{display:block;height:2px;background:var(--red)}
.chart-card{position:absolute;left:692px;top:181px;width:295px;height:184px;border:1px solid var(--card-border);border-radius:10px;background:rgba(23,38,63,.7);padding:20px 19px}
.chart-card h4{font-size:10.5px;font-weight:600;display:flex;align-items:center;gap:6px}
.chart-card svg.chart{position:absolute;left:19px;top:90px}
.testimonials{height:418px;background:var(--mist);position:relative;overflow:hidden}
.testimonials .section-title{position:absolute;top:70px;left:0;right:0}
.testimonials .section-sub{position:absolute;top:122px;left:0;right:0}
.quote-row{position:absolute;top:180px;left:25px;display:flex;gap:20px}
.quote{width:219px;height:179px;background:var(--white);border-radius:10px;padding:22px 20px 0}
.stars{color:var(--red);font-size:9px;letter-spacing:2px}
.quote p{margin-top:10px;font-size:10px;line-height:17.8px;color:#2a3346}
.who{margin-top:12px;display:flex;align-items:center;gap:8px}
.avatar{width:28px;height:28px;border-radius:50%;background:var(--mist);display:flex;align-items:center;justify-content:center;font-size:9.5px;font-weight:700;color:#3a4458}
.who strong{display:block;font-size:9.5px;font-weight:600}
.who span{display:block;font-size:7.8px;color:var(--muted);margin-top:2px}
.fade-left{position:absolute;top:0;bottom:0;left:0;width:250px;background:linear-gradient(90deg,rgba(232,236,241,.85),rgba(232,236,241,0))}
.fade-right{position:absolute;top:0;bottom:0;right:0;width:250px;background:linear-gradient(270deg,rgba(232,236,241,.85),rgba(232,236,241,0))}
.contact{height:389px;position:relative}
.contact-card{position:absolute;left:223px;top:65px;width:764px;height:259px;border-radius:22px;background:linear-gradient(135deg,#0f1d35 0%,#13203b 65%,#1d2140 100%);box-shadow:0 18px 36px rgba(15,29,53,.25);color:var(--white)}
.contact-info{position:absolute;left:36px;top:42px;width:280px}
.contact-info h2{font-size:22px;font-weight:400}
.contact-info p{margin-top:14px;font-size:10.5px;line-height:17.5px;color:#c9d0db}
.contact-list{margin-top:20px;list-style:none}
.contact-list li{display:flex;align-items:center;gap:8px;font-size:10px;height:22px}
.contact-list b{font-weight:600}
.contact-form{position:absolute;left:398px;top:39px;width:330px}
.field{height:33px;border-radius:8px;background:rgba(255,255,255,.05);border:1px solid rgba(255,255,255,.1);font-size:9.5px;color:#8d97a8;padding:0 13px;line-height:33px}
.field-row{display:flex;gap:10px}
.field-row .field{flex:1}
.field.area{height:63px;line-height:normal;padding-top:12px}
.send{margin-top:10px;height:32px;border-radius:16px;background:var(--red);box-shadow:0 6px 16px rgba(200,16,46,.35);font-size:10.5px;font-weight:600;display:flex;align-items:center;justify-content:center}
.site-footer{height:68px;background:var(--navy);position:relative;color:#a9b2c1;font-size:8.5px}
.footer-brand{position:absolute;left:223px;top:24px;color:var(--white);font-weight:700;font-size:10px;letter-spacing:.04em;display:flex;align-items:center;gap:6px}
.footer-links{position:absolute;left:418px;top:29px;display:flex;gap:18px}
.copyright{position:absolute;right:213px;top:29px}
</style>
</head>
<body>

<section class="hero">
  <div class="hero-photo" role="img" aria-label="Modern house with glass walls at dusk beneath large trees"></div>
  <div class="hero-shade"></div>
  <header class="site-header">
    <div class="brand"><span class="brand-dot"></span>TALLGROVE VALE</div>
    <nav class="nav">
      <a href="#">Services</a>
      <a href="#">Investors</a>
      <a href="#">Testimonials</a>
      <a href="#" class="btn-nav">Get Started</a>
    </nav>
  </header>
  <div class="hero-content">
    <span class="badge">✦ TRUSTED ASSET MANAGEMENT</span>
    <h1>Where <span class="accent">Capital</span><br>Meets<br><span class="accent">Confidence</span></h1>
    <p>Tallgrove Vale Management delivers premium property solutions for discerning investors. Unmatched performance, absolute transparency.</p>
    <div class="hero-actions">
      <div class="btn btn-primary">Start Investing</div>
      <div class="btn btn-ghost">Explore Services</div>
    </div>
  </div>
</section>

<section class="services">
  <h2 class="section-title">Premium <span class="accent">Services</span></h2>
  <p class="section-sub">Full-service property management backed by data, design, and decades of expertise.</p>
  <div class="service-grid">
    <article class="service-card">
      <svg viewBox="0 0 30 30"><rect x="6" y="4" width="18" height="24" rx="1.5" fill="#7d8fa8"/><g fill="#bfe0f5"><rect x="9" y="7" width="3" height="3"/><rect x="13.5" y="7" width="3" height="3"/><rect x="18" y="7" width="3" height="3"/><rect x="9" y="12" width="3" height="3"/><rect x="13.5" y="12" width="3" height="3"/><rect x="18" y="12" width="3" height="3"/><rect x="9" y="17" width="3" height="3"/><rect x="18" y="17" width="3" height="3"/></g><rect x="13" y="22" width="4" height="6" fill="#4a5568"/></svg>
      <h3>Acquisition &amp; Sourcing</h3>
      <p>Off-market deals, institutional-grade underwriting, and prime location targeting.</p>
      <span class="more">Learn more →</span>
    </article>
    <article class="service-card">
      <svg viewBox="0 0 30 30"><rect x="3" y="3" width="24" height="24" rx="3" fill="#e8edf3"/><rect x="7" y="14" width="4" height="10" fill="#3bb273"/><rect x="13" y="8" width="4" height="16" fill="#e2335a"/><rect x="19" y="11" width="4" height="13" fill="#3a7bd5"/></svg>
      <h3>Asset Management</h3>
      <p>Active value-add strategies, lease optimization, and portfolio performance tracking.</p>
      <span class="more">Learn more →</span>
    </article>
    <article class="service-card">
      <svg viewBox="0 0 30 30"><path d="M8 5a5 5 0 0 0 5 7l11 11a2 2 0 0 1-3 3L10 15a5 5 0 0 1-6-6l3 3 3-1 1-3-3-3z" fill="#aab3c2"/></svg>
      <h3>Property Operations</h3>
      <p>24/7 maintenance, tenant relations, and capital improvement project management.</p>
      <span class="more">Learn more →</span>
    </article>
    <article class="service-card">
      <svg viewBox="0 0 30 30"><rect x="3" y="3" width="24" height="24" rx="3" fill="#eef1f6" stroke="#c9d1dd"/><path d="M3 11h24M3 19h24M11 3v24M19 3v24" stroke="#dbe1ea"/><path d="M6 23l6-7 5 3 8-10" stroke="#3a7bd5" stroke-width="2" fill="none"/></svg>
      <h3>Investor Reporting</h3>
      <p>Real-time dashboards, quarterly valuations, and transparent fee structures.</p>
      <span class="more">Learn more →</span>
    </article>
  </div>
</section>

<section class="dashboard">
  <h2 class="section-title">Investor <span class="accent">Dashboard</span></h2>
  <p class="section-sub">Live portfolio intelligence — performance at a glance.</p>
  <div class="stat" style="left:223px;top:172px"><div class="value">$184.2<span class="accent">M</span></div><div class="label">Total Equity Value</div><div class="bar"><span style="width:82%"></span></div></div>
  <div class="stat" style="left:451px;top:172px"><div class="value">9.8<span class="accent">%</span></div><div class="label">Portfolio Yield</div><div class="bar"><span style="width:68%"></span></div></div>
  <div class="stat" style="left:223px;top:279px"><div class="value">32</div><div class="label">Active Properties</div><div class="bar"><span style="width:54%"></span></div></div>
  <div class="stat" style="left:451px;top:279px"><div class="value">94<span class="accent">%</span></div><div class="label">Occupancy Rate</div><div class="bar"><span style="width:94%"></span></div></div>
  <div class="chart-card">
    <h4><svg width="10" height="10" viewBox="0 0 10 10"><rect x="0.5" y="1.5" width="9" height="8" rx="1" fill="#8ea0bd"/><rect x="0.5" y="1.5" width="9" height="2.5" fill="#c8d2e2"/></svg>Quarterly NAV Growth</h4>
    <svg class="chart" width="258" height="80" viewBox="0 0 258 80" font-family="Inter, sans-serif" font-size="6.5" text-anchor="middle">
      <text x="29" y="10" fill="#8793a6">$142M</text>
      <rect x="0" y="16" width="58" height="30" fill="#4a1a33"/>
      <text x="96" y="9" fill="#8793a6">$158M</text>
      <rect x="67" y="15" width="58" height="31" fill="#4a1a33"/>
      <text x="162" y="33" fill="#8793a6">$171M</text>
      <rect x="133" y="40" width="58" height="6" fill="#4a1a33"/>
      <text x="229" y="33" fill="#ffffff" font-weight="600">$184M</text>
      <rect x="200" y="40" width="58" height="6" rx="1" fill="#c8102e"/>
      <g fill="#6c7789"><text x="29" y="67">Q1</text><text x="96" y="67">Q2</text><text x="162" y="67">Q3</text><text x="229" y="67">Q4</text></g>
    </svg>
  </div>
</section>

<section class="testimonials">
  <h2 class="section-title">What <span class="accent">Investors</span> Say</h2>
  <p class="section-sub">Real feedback from partners who trust us with their capital.</p>
  <div class="quote-row">
    <article class="quote"><div class="stars">★★★★★</div><p>“The dashboard gives us real-time clarity. Tallgrove Vale Management operates with the precision of a Fortune 500 firm.”</p><div class="who"><div class="avatar">TK</div><div><strong>Tobias Kerrane</strong><span>Private Equity Partner</span></div></div></article>
    <article class="quote"><div class="stars">★★★★★</div><p>“From acquisition to exit, they handled everything flawlessly. A true partner in every sense of the word.”</p><div class="who"><div class="avatar">SW</div><div><strong>Selena Whitmore</strong><span>High-Net-Worth Investor</span></div></div></article>
    <article class="quote"><div class="stars">★★★★★</div><p>“Their underwriting is conservative, their execution is aggressive. That’s a rare combination in this industry.”</p><div class="who"><div class="avatar">DL</div><div><strong>Daniel Lorne</strong><span>Fund Manager</span></div></div></article>
    <article class="quote"><div class="stars">★★★★★</div><p>“Tallgrove Vale Management transformed our portfolio. Their operational rigor and market insight are unmatched.”</p><div class="who"><div class="avatar">JD</div><div><strong>Jonah Dell</strong><span>Family Office Principal</span></div></div></article>
    <article class="quote"><div class="stars">★★★★★</div><p>“We’ve seen consistent 14%+ returns across three cycles. Their team is proactive, transparent, and deeply experienced.”</p><div class="who"><div class="avatar">MR</div><div><strong>Mara Ridley</strong><span>Institutional Investor</span></div></div></article>
  </div>
  <div class="fade-left"></div>
  <div class="fade-right"></div>
</section>

<section class="contact">
  <div class="contact-card">
    <div class="contact-info">
      <h2>Ready to <span class="accent">Partner</span> with Us?</h2>
      <p>Connect with our team to explore investment opportunities or discuss your property management needs.</p>
      <ul class="contact-list">
        <li><svg width="11" height="11" viewBox="0 0 24 24"><path d="M6.6 10.8a15 15 0 0 0 6.6 6.6l2.2-2.2a1 1 0 0 1 1-.25 11.4 11.4 0 0 0 3.6.6 1 1 0 0 1 1 1V20a1 1 0 0 1-1 1A17 17 0 0 1 3 4a1 1 0 0 1 1-1h3.5a1 1 0 0 1 1 1c0 1.25.2 2.45.6 3.6a1 1 0 0 1-.25 1z" fill="#e2335a"/></svg><b>Call:</b> (380) 555-0142</li>
        <li><svg width="11" height="11" viewBox="0 0 24 24"><rect x="2" y="5" width="20" height="14" rx="1" fill="#aab3c2"/><path d="M2 6l10 7 10-7" stroke="#6b7587" fill="none"/></svg><b>Email:</b> invest@tallgrovevalemanagement.com</li>
        <li><svg width="11" height="11" viewBox="0 0 24 24"><path d="M12 2a7 7 0 0 0-7 7c0 5 7 13 7 13s7-8 7-13a7 7 0 0 0-7-7z" fill="#e2335a"/><circle cx="12" cy="9" r="2.5" fill="#fff"/></svg><b>Office:</b> 240 Harbor Lane, Alder Falls, OH 43009</li>
      </ul>
    </div>
    <form class="contact-form">
      <div class="field-row"><div class="field">Full name</div><div class="field">Email address</div></div>
      <div class="field" style="margin-top:2px">Phone number</div>
      <div class="field area" style="margin-top:10px">Tell us about your investment goals...</div>
      <div class="send">Send Inquiry →</div>
    </form>
  </div>
</section>

<footer class="site-footer">
  <div class="footer-brand"><span class="brand-dot"></span>TALLGROVE VALE</div>
  <nav class="footer-links"><span>Privacy</span><span>Terms</span><span>Disclosures</span><span>Careers</span></nav>
  <div class="copyright">© 2026 Tallgrove Vale Management. All rights reserved.</div>
</footer>

</body>
</html>
```